5868 7090

Web(re)design of an existing directory search site www.le7090x.be (in Dutch www.de5868x.be and in English www.3969x.be).

This site is a directory site, i.e. a "white pages" site whereby people can search the phone & details of another person based on a combination of name + city (for instance darrow in Brussels); one can also search a company also based on a combination of name + city (for instance Vornex in Brussels); last but not least one can also search the name of the subscriber behind a specific telephone number (also called reverse search).

This site is quite outdated and needs a redesign, see instructions.

We need the output in XD format.

```html
<!DOCTYPE html>
<html lang="en">
<head>
<meta charset="utf-8">
<title>7090 – Directory search</title>
<link href="https://fonts.googleapis.com/css2?family=Roboto:wght@400;500;700&family=Tinos&display=swap" rel="stylesheet">
<style>
:root{
  --red-1:#d40000;
  --red-2:#7c0000;
  --seg-1:#fce3e4;
  --seg-2:#fcc5c6;
  --seg-3:#fba9aa;
  --seg-btn:#f85757;
  --ink:#1e1e1e;
  --muted:#444;
  --about-bg:#f4f4f4;
  --footer-bg:#4a0000;
  --white:#fff;
}
*{margin:0;padding:0;box-sizing:border-box}
html,body{width:1200px;height:842px;overflow:hidden}
body{font-family:"Roboto",sans-serif;color:var(--ink);background:var(--white);position:relative}
.header{position:absolute;left:0;top:0;width:1200px;height:42.5px;background:var(--white);z-index:3}
.brand{position:absolute;left:222px;top:-6px;width:62px;height:64px;border-radius:50%;background:var(--white);display:flex;align-items:center;justify-content:center}
.brand-name{font-weight:700;font-size:15px;color:var(--red-1);margin-top:4px}
.nav{position:absolute;left:541px;top:13px;display:flex;gap:24px;font-size:13px}
.nav a{color:var(--ink);text-decoration:none;padding-bottom:2px}
.nav a.active{border-bottom:1px solid var(--red-1)}
.account{position:absolute;left:953px;top:12px}
.hero{position:absolute;left:0;top:42.5px;width:1200px;height:312.5px;background:linear-gradient(100deg,var(--red-1),#a80000 55%,var(--red-2))}
.hero-title{position:absolute;top:54px;width:100%;text-align:center;font-family:"Tinos",serif;font-size:23px;color:var(--white)}
.search{position:absolute;left:287.5px;top:115.5px;width:625px;height:44px;border-radius:22px;overflow:hidden;display:flex}
.search .field{width:187.5px;height:44px;font-size:10px;color:#555;display:flex;align-items:center}
.f-name{background:var(--seg-1);padding-left:19px}
.f-city{background:var(--seg-2);padding-left:32px}
.f-number{background:var(--seg-3);padding-left:16px}
.search .go{width:62.5px;background:var(--seg-btn);display:flex;align-items:center;justify-content:center}
.popular-title{position:absolute;top:191px;width:100%;text-align:center;font-size:14px;color:var(--white)}
.tags{position:absolute;top:222px;width:100%;text-align:center;color:var(--white);font-size:10px;line-height:20px}
.tags span{margin:0 2.5px}
.about{position:absolute;left:0;top:355px;width:1200px;height:301px;background:var(--about-bg)}
.about-art{position:absolute;left:213px;top:45px;width:312px;height:207px;background:linear-gradient(135deg,#f4a48a,#e8553a 50%,#f7b7a8);border-radius:4px}
.about-title{position:absolute;left:600px;width:373px;top:36px;text-align:center;font-size:30px;font-weight:700}
.about-text{position:absolute;left:600px;top:96px;width:375px;font-size:10px;line-height:16.3px;color:var(--muted)}
.about-text p{margin-bottom:3px}
.footer{position:absolute;left:0;top:656px;width:1200px;height:186px;background:var(--footer-bg);color:var(--white)}
.footer h3{position:absolute;top:35px;font-size:12.5px;font-weight:700}
.footer ul{position:absolute;top:72px;list-style:none;font-size:10px;line-height:20.7px}
.contact{position:absolute;left:846px;top:72px;font-size:10px}
.contact li{list-style:none;display:flex;align-items:flex-start;gap:13px;margin-bottom:8.5px;line-height:12px}
.contact svg{flex:none;width:12px;height:12px}
.copyright{position:absolute;top:157px;width:100%;text-align:center;font-size:10px}
</style>
</head>
<body>
<header class="header">
  <div class="brand"><span class="brand-name">7090</span></div>
  <nav class="nav"><a class="active" href="#">Home</a><a href="#">Contact us</a></nav>
  <svg class="account" width="19" height="19" viewBox="0 0 20 20" fill="none" stroke="#222" stroke-width="1.3"><circle cx="10" cy="10" r="9"/><circle cx="10" cy="7.5" r="3.2"/><path d="M4 16c1.5-2.6 3.5-3.6 6-3.6s4.5 1 6 3.6"/></svg>
</header>

<section class="hero">
  <h1 class="hero-title" style="font-weight:400">Everything you need is here! Just search any keyword.</h1>
  <form class="search">
    <div class="field f-name">Name...</div>
    <div class="field f-city">City...</div>
    <div class="field f-number">Number...</div>
    <div class="go"><svg width="18" height="18" viewBox="0 0 20 20" fill="none" stroke="#fff" stroke-width="1.4"><circle cx="8.5" cy="8.5" r="7"/><path d="M13.5 13.5l5.5 5.5"/></svg></div>
  </form>
  <h2 class="popular-title" style="font-weight:400">Recent popular search</h2>
  <div class="tags">
    <div><span>#lorem</span><span>#ipsum</span><span>#doller</span><span>#amit</span><span>#lipu</span><span>#loremipsum</span><span>#sumer</span><span>#tapos</span></div>
    <div><span>#lorem</span><span>#impsu</span><span>#trmvfo</span><span>#ipsum</span><span>#doller</span><span>#amit</span><span>#lipu</span><span>#loremipsum</span><span>#sumer</span><span>#tapos</span></div>
    <div><span>#lorem</span><span>#ipsum</span><span>#doller</span><span>#amit</span><span>#lipu</span><span>#loremipsum</span><span>#sumer</span><span>#tapos</span></div>
  </div>
</section>

<section class="about">
  <div class="about-art" role="img" aria-label="Illustration of a person at a computer searching data with a magnifying glass"></div>
  <h2 class="about-title">About Us</h2>
  <div class="about-text">
    <p>orem ipsum dolor sit amet, consectetur adipiscing elit. Proin vel pretium tellus, eu elementum justo. Aliquam eget euismod magna. Aenean efficitur, velit in bibendum aliquam, turpis sapien ornare tellus.</p>
    <p>sed dignissim purus ipsum eget ipsum. Proin tempor commodo magna ut pharetra. Sed vulputate velit arcu, aliquam vehicula dui condimentum nec. Morbi a orci erat. Etiam tincidunt consequat ligula ac viverra. Orci varius natoque penatibus et magnis dis parturient montes, nascet</p>
    <p>ascetur ridiculus mus. Cras sed eros lectus. Phasellus sem tortor, varius ac sem et, rhoncus consectetur mi. Donec vehicula efficitur nisi id blandit. Etiam vel pellentesque libero, nec ornare odio.</p>
  </div>
</section>

<footer class="footer">
  <h3 style="left:220px">Search</h3>
  <ul style="left:220px"><li>Custom search</li><li>Category A-Z</li><li>Keyword A-Z</li></ul>
  <h3 style="left:477px">Our Organisation</h3>
  <ul style="left:477px"><li>About us</li><li>Terms</li><li>Condition</li></ul>
  <ul style="left:604px"><li>Cookies</li><li>Customer Services</li><li>Review Policies</li></ul>
  <h3 style="left:846px">Locate us</h3>
  <ul class="contact" style="top:72px">
    <li><svg viewBox="0 0 24 24" fill="#fff"><path d="M6.6 10.8a15 15 0 006.6 6.6l2.2-2.2c.3-.3.7-.4 1-.2 1.1.4 2.3.6 3.6.6.6 0 1 .4 1 1V20c0 .6-.4 1-1 1A17 17 0 013 4c0-.6.4-1 1-1h3.5c.6 0 1 .4 1 1 0 1.2.2 2.4.6 3.6.1.3 0 .7-.2 1z"/></svg><span>+1-23-4871</span></li>
    <li><svg viewBox="0 0 24 24" fill="#fff"><path d="M2 5h20v14H2z"/><path d="M2 5l10 8 10-8" stroke="#4a0000" stroke-width="2" fill="none"/></svg><span>info@7090x.com</span></li>
    <li><svg viewBox="0 0 24 24" fill="#fff"><path d="M12 2a7 7 0 00-7 7c0 5 7 13 7 13s7-8 7-13a7 7 0 00-7-7zm0 9.5A2.5 2.5 0 1112 6.5a2.5 2.5 0 010 5z"/></svg><span>Maple Ave, 2nd St<br>418207 NY</span></li>
  </ul>
  <div class="copyright">Copyright ODR 2010, tous droits réservés</div>
</footer>
</body>
</html>
```